Copperleaf Motorized Shade Business Card

Hello, we've had our logo made. Now we are looking for a clean and cool looking business card. One side can just be the logo with any design elements that might look good with it. The other side will be Name, Phone Number and Email. There will not be an address on the card.

```html
<!DOCTYPE html>
<html lang="en">
<head>
<meta charset="utf-8">
<title>Copperleaf Motorized Shade — Business Card</title>
<link href="https://fonts.googleapis.com/css2?family=Montserrat:wght@400;500;700;800&display=swap" rel="stylesheet">
<style>
  :root {
    --navy: #0b3a75;
    --sky: #1fa6e6;
    --sun: #f8bf1c;
    --card: #ffffff;
    --edge: #cfe6f3;
    --backdrop: #8e8f93;
  }
  * { box-sizing: border-box; margin: 0; padding: 0; }
  html, body { width: 1200px; height: 913px; overflow: hidden; }
  body {
    background: var(--backdrop);
    font-family: "Montserrat", Arial, sans-serif;
    position: relative;
  }
  .card {
    position: absolute;
    width: 560px;
    height: 320px;
    background: var(--card);
    border-radius: 18px;
    box-shadow: 0 5px 0 var(--edge), 0 10px 0 #bcdcee, 0 16px 24px rgba(0,0,0,.25);
  }
  .card--front { left: 60px; top: 70px; }
  .card--back { left: 580px; top: 500px; }

  .wordmark {
    display: flex;
    align-items: center;
    gap: 14px;
  }
  .wordmark__mark {
    width: 22px; height: 22px;
    background: var(--sun);
    flex: none;
  }
  .wordmark__name {
    color: var(--navy);
    font-weight: 800;
    text-transform: uppercase;
    line-height: 1.05;
    letter-spacing: .02em;
  }
  .card--front .wordmark {
    position: absolute;
    left: 50%; top: 50%;
    transform: translate(-50%, -50%);
  }
  .card--front .wordmark__name { font-size: 34px; }
  .card--front .wordmark__mark { width: 34px; height: 34px; }

  .card--back .wordmark {
    position: absolute;
    right: 40px; top: 44px;
  }
  .card--back .wordmark__name { font-size: 21px; }

  .contact {
    position: absolute;
    left: 46px; bottom: 40px;
  }
  .contact__name {
    color: var(--navy);
    font-weight: 700;
    font-size: 22px;
    letter-spacing: .03em;
    text-transform: uppercase;
  }
  .contact__role {
    color: var(--sky);
    font-weight: 500;
    font-size: 13px;
    letter-spacing: .04em;
    text-transform: uppercase;
    margin-bottom: 18px;
  }
  .contact__list { list-style: none; }
  .contact__item {
    display: flex;
    align-items: center;
    gap: 10px;
    color: var(--navy);
    font-size: 15px;
    line-height: 24px;
  }
  .contact__icon { width: 15px; height: 15px; flex: none; fill: var(--sky); }
</style>
</head>
<body>
  <section class="card card--front" aria-label="Card front">
    <div class="wordmark">
      <span class="wordmark__mark"></span>
      <span class="wordmark__name">Copperleaf<br>Motorized Shade</span>
    </div>
  </section>

  <section class="card card--back" aria-label="Card back">
    <div class="wordmark">
      <span class="wordmark__mark"></span>
      <span class="wordmark__name">Copperleaf<br>Motorized Shade</span>
    </div>

    <div class="contact">
      <p class="contact__name">Dana Whitfield</p>
      <p class="contact__role">Director</p>
      <ul class="contact__list">
        <li class="contact__item">
          <svg class="contact__icon" viewBox="0 0 24 24" aria-hidden="true"><path d="M6.6 10.8a15.1 15.1 0 0 0 6.6 6.6l2.2-2.2a1 1 0 0 1 1-.25 11.4 11.4 0 0 0 3.6.57 1 1 0 0 1 1 1V20a1 1 0 0 1-1 1A17 17 0 0 1 3 4a1 1 0 0 1 1-1h3.5a1 1 0 0 1 1 1c0 1.25.2 2.45.57 3.57a1 1 0 0 1-.25 1z"/></svg>
          5550142290
        </li>
        <li class="contact__item">
          <svg class="contact__icon" viewBox="0 0 24 24" aria-hidden="true"><path d="M2 5h20v14H2z M3.5 6.5 12 13l8.5-6.5" fill="none" stroke="#1fa6e6" stroke-width="2"/></svg>
          info@copperleafshade.com
        </li>
        <li class="contact__item">
          <svg class="contact__icon" viewBox="0 0 24 24" aria-hidden="true"><circle cx="12" cy="12" r="9" fill="none" stroke="#1fa6e6" stroke-width="2"/><path d="M3 12h18M12 3c3 3 3 15 0 18M12 3c-3 3-3 15 0 18" fill="none" stroke="#1fa6e6" stroke-width="1.6"/></svg>
          www.copperleafshade.com
        </li>
      </ul>
    </div>
  </section>
</body>
</html>
```